Tallmark Benefit Advisors Business Card Design

I already placed order for cards through press grove.

Double sided- back Navy with White logo and raised silver "swoosh"

```html
<!DOCTYPE html>
<html lang="en">
<head>
<meta charset="utf-8">
<title>Tallmark Benefit Advisors – Business Card</title>
<link href="https://fonts.googleapis.com/css2?family=Open+Sans:wght@400;600;700&display=swap" rel="stylesheet">
<style>
  :root {
    --navy: #0f2146;
    --navy-deep: #0b1b3d;
    --silver: #b9bcc2;
    --ink-grey: #4a4d55;
    --paper: #ffffff;
    --stage: #e6e7ea;
  }
  * { box-sizing: border-box; margin: 0; padding: 0; }
  html, body {
    width: 1200px; height: 689px; overflow: hidden;
    background: var(--stage);
    font-family: "Open Sans", Arial, sans-serif;
  }
  .sheet {
    position: relative; width: 1200px; height: 689px;
    display: flex; align-items: center; justify-content: center; gap: 60px;
  }
  .card {
    position: relative; width: 520px; height: 297px;
    box-shadow: 0 10px 28px rgba(0,0,0,.18);
    overflow: hidden;
  }
  /* front */
  .card-front { background: var(--paper); color: var(--navy); }
  .front-wordmark { position: absolute; left: 34px; top: 30px; }
  .front-wordmark .brand-name {
    font-weight: 600; font-size: 30px; letter-spacing: 1px; line-height: 1;
  }
  .front-wordmark .brand-sub {
    font-weight: 600; font-size: 10px; letter-spacing: 5.4px; margin-top: 4px;
  }
  .person { position: absolute; left: 34px; top: 104px; }
  .person .name { font-weight: 700; font-size: 19px; letter-spacing: .5px; }
  .person .role { font-size: 12px; color: var(--ink-grey); margin-top: 1px; }
  .contact-list {
    position: absolute; left: 34px; top: 160px; list-style: none;
    font-size: 11px; color: var(--ink-grey); line-height: 1.45;
  }
  .contact-list li { display: flex; align-items: flex-start; gap: 8px; }
  .contact-list svg { width: 10px; height: 10px; fill: var(--navy); flex: none; margin-top: 3px; }
  .front-mark {
    position: absolute; right: 28px; bottom: 22px;
    display: flex; align-items: center; gap: 10px;
    font-weight: 700; font-size: 40px; color: var(--navy); line-height: 1;
  }
  .front-mark .dot { width: 16px; height: 16px; border-radius: 50%; background: var(--silver); }
  /* back */
  .card-back {
    background: var(--navy-deep);
    display: flex; align-items: center; justify-content: center; gap: 22px;
  }
  .back-short { font-weight: 600; font-size: 34px; color: var(--paper); }
  .back-rule { width: 1px; height: 70px; background: var(--silver); }
  .back-wordmark { color: var(--paper); font-weight: 600; }
  .back-wordmark .brand-name { font-size: 30px; letter-spacing: 1px; line-height: 1; }
  .back-wordmark .brand-sub { font-size: 10px; letter-spacing: 5.4px; margin-top: 5px; }
</style>
</head>
<body>
<main class="sheet">
  <section class="card card-front" aria-label="Card front">
    <div class="front-wordmark">
      <div class="brand-name">TALLMARK</div>
      <div class="brand-sub">BENEFIT ADVISORS</div>
    </div>
    <div class="person">
      <div class="name">DANIEL REYES</div>
      <div class="role">Founder &amp; CEO</div>
    </div>
    <ul class="contact-list">
      <li><svg viewBox="0 0 10 10"><path d="M5 0a3.5 3.5 0 0 0-3.5 3.5C1.5 6 5 10 5 10s3.5-4 3.5-6.5A3.5 3.5 0 0 0 5 0zm0 5a1.5 1.5 0 1 1 0-3 1.5 1.5 0 0 1 0 3z"/></svg><span>423 Street Address Here, City<br>State &amp; Country, ZIP Code</span></li>
      <li><svg viewBox="0 0 10 10"><path d="M2 0l2 2.5-1 1.2a6 6 0 0 0 3.3 3.3l1.2-1L10 8l-1.5 2C4 10 0 6 0 1.5z"/></svg><span>(123) 456-7890</span></li>
      <li><svg viewBox="0 0 10 10"><path d="M2.5 0h5v10h-5zM3.5 1v7h3V1z"/></svg><span>(123) 456-7890</span></li>
      <li><svg viewBox="0 0 10 10"><path d="M2.5 0h5v3h-5zM0 3.5h10v4H8V10H2V7.5H0zM3 6v3h4V6z"/></svg><span>(123) 456-7890</span></li>
      <li><svg viewBox="0 0 10 10"><path d="M0 2h10v6H0zm1 1v.3l4 2.5 4-2.5V3z"/></svg><span>info@tallmarkadvisors.com</span></li>
      <li><svg viewBox="0 0 10 10"><circle cx="5" cy="5" r="5"/><path d="M0 5h10M5 0v10" stroke="#fff" stroke-width=".8"/></svg><span>tallmarkadvisors.com</span></li>
    </ul>
    <div class="front-mark"><span class="dot"></span><span>Tallmark</span></div>
  </section>

  <section class="card card-back" aria-label="Card back">
    <div class="back-short">Tallmark</div>
    <div class="back-rule"></div>
    <div class="back-wordmark">
      <div class="brand-name">TALLMARK</div>
      <div class="brand-sub">BENEFIT ADVISORS</div>
    </div>
  </section>
</main>
</body>
</html>
```